Dental Health Door hanger for contest to attract new patients

We are a group dental practice located in Burlington, Ontario, Canada. We are looking to bring in new patients and are targeting a new subdivision as well as established neighbourhoods around it.

The door hanger we require is for a contest are offering that will run for approx. 6 months to win a $1000.00 travel gift card. The individual must come in person to drop off the ballot and during that time they will get a tour of the practice and meet key people. There is no requirement for them to make an appointment but that is the ultimate goal.

I have included:
- a picture we typically use, however it is not required (female smiling)
- Our logo with "your city your dentists" below it. We want that tagline removed
- our other logo
- the excel version of the map created to our location
- the current one attempted on our own and is missing something - like the concept but not the total look/ feel

The final design should make the person want to come in and book an appointment with us and at the very least call to schedule something with a dentist.

Target Market(s)

New subdivision and surrounding area for new patients

Industry/Entity Type

Dental Clinic

Colors

Designer to choose colors to be used in the design.

Requirements
Must have
• Our address is 1846 Pinecrest Road, Burlington, Ontario L7N 2R8. Our phone number is 905-418-2735. We are located on the 3rd floor of the Marden Family Health Centre.
Nice to have
• We only need to have a logo, our address, a ballot of some sort on the door hanger and the details about the contest, the rest is up to you. We are moving towards the slogan "what makes you smile" at some point so this can be incorporated if it works with the overall design.
Should not have
• Fluorescent colours

```html
<!DOCTYPE html>
<html lang="en">
<head>
<meta charset="utf-8">
<title>What makes you smile – Door Hanger</title>
<link href="https://fonts.googleapis.com/css2?family=Montserrat:wght@600;700&display=swap" rel="stylesheet">
<style>
  :root {
    --plum: #51296b;
    --crimson: #d8303a;
    --ink: #1e1c1d;
    --white: #ffffff;
    --brick: #a8282e;
    --brand-blue: #6a88c0;
    --backdrop: #e6e6e6;
  }
  html, body { margin: 0; padding: 0; overflow: hidden; background: var(--backdrop); }
  .hanger {
    position: relative;
    width: 861px;
    height: 1200px;
    overflow: hidden;
    font-family: "Montserrat", sans-serif;
    font-weight: 700;
    background: var(--white);
  }
  .layer { position: absolute; left: 0; top: 0; }
  .hero-photo {
    position: absolute;
    left: 0; top: 180px;
    width: 861px; height: 540px;
    background:
      radial-gradient(ellipse 28% 38% at 52% 48%, #e6c2ae 0%, #c99b86 45%, transparent 75%),
      linear-gradient(100deg, #3a2b26 0%, #5b4338 30%, #b9a39a 60%, #e8dcd6 85%, #f3ece8 100%);
  }
  .brand {
    position: absolute;
    left: 60px; top: 24px;
    display: flex; align-items: center; gap: 14px;
  }
  .brand-mark { width: 40px; height: 40px; background: var(--brand-blue); }
  .brand-name {
    color: var(--brand-blue);
    font-size: 33px; line-height: 40px;
    margin: 0;
  }
  .slogan {
    position: absolute;
    left: 367px; top: 46px; width: 494px;
    margin: 0;
    text-align: center;
    color: var(--white);
    font-size: 42px; line-height: 52px; font-weight: 700;
  }
  .walker { position: absolute; left: 74px; top: 702px; }
  .visit-note {
    position: absolute;
    left: 71px; top: 765px;
    color: var(--white);
    font-size: 27px; line-height: 35px;
    margin: 0;
  }
  .ballot {
    position: absolute;
    left: 71px; top: 1128px; width: 262px;
    border: 2px dashed var(--white);
    padding: 6px 10px;
    box-sizing: border-box;
    color: var(--white);
    font-size: 17px; line-height: 26px;
  }
  .ballot-row { display: flex; align-items: baseline; gap: 8px; }
  .ballot-line { flex: 1; border-bottom: 2px solid var(--white); height: 18px; }
  .prize {
    position: absolute;
    left: 422px; top: 676px;
    color: var(--crimson);
    font-size: 78px; line-height: 94px;
  }
  .prize-note {
    position: absolute;
    left: 430px; top: 770px;
    color: var(--white);
    font-size: 20px; line-height: 24px;
    letter-spacing: 2px;
  }
  .contest-details {
    position: absolute;
    left: 430px; top: 812px;
    color: var(--white);
    font-size: 35px; line-height: 42px;
    margin: 0;
  }
  .contest-details .call-to-action { color: var(--crimson); }
  .contact {
    position: absolute;
    left: 367px; top: 1042px; width: 494px; height: 158px;
    background: var(--white);
  }
  .contact-icon { position: absolute; }
  .phone {
    position: absolute; left: 113px; top: 12px;
    color: var(--brick); font-size: 35px;
  }
  .web {
    position: absolute; left: 96px; top: 64px;
    color: var(--brick); font-size: 19px;
  }
  .address {
    position: absolute; left: 60px; top: 92px; width: 410px;
    color: var(--brick); font-size: 19px; line-height: 25px;
    text-align: center;
  }
</style>
</head>
<body>
<div class="hanger">

  <div class="hero-photo" role="img" aria-label="Photo of a smiling young woman in a knit winter hat and scarf"></div>

  <svg class="layer" width="861" height="1200" viewBox="0 0 861 1200" aria-hidden="true">
    <defs>
      <linearGradient id="band" x1="0" y1="0" x2="0" y2="1">
        <stop offset="0" stop-color="#51296b"/>
        <stop offset="1" stop-color="#d8303a"/>
      </linearGradient>
      <linearGradient id="panel" x1="0" y1="0" x2="0" y2="1">
        <stop offset="0" stop-color="#4e2a6b"/>
        <stop offset="1" stop-color="#d8303a"/>
      </linearGradient>
    </defs>
    <path class="top-band" d="M0 0 H861 V200 Q620 252 367 245 Q180 238 0 195 Z" fill="url(#band)"/>
    <path class="logo-panel" d="M36 0 H367 V245 Q200 237 36 200 Z" fill="#ffffff"/>
    <path class="lower-field" d="M0 692 Q180 650 367 648 Q620 652 861 696 V1200 H0 Z" fill="#1e1c1d"/>
    <path class="visit-panel" d="M36 684 Q200 652 367 648 V1200 H36 Z" fill="url(#panel)"/>
    <g class="hanger-cut" fill="#e6e6e6">
      <circle cx="614" cy="26" r="16"/>
      <rect x="611" y="0" width="6" height="20"/>
    </g>
  </svg>

  <div class="brand">
    <div class="brand-mark"></div>
    <p class="brand-name">Brightway<br>Dental<br>Group</p>
  </div>

  <h1 class="slogan">What makes<br>you smile</h1>

  <svg class="walker" width="44" height="50" viewBox="0 0 44 50" aria-hidden="true">
    <g fill="none" stroke="#d8303a" stroke-width="5" stroke-linecap="round" stroke-linejoin="round">
      <circle cx="28" cy="6" r="4" fill="#d8303a" stroke="none"/>
      <path d="M24 15 L18 30 L10 46"/>
      <path d="M18 30 L28 36 L30 46"/>
      <path d="M22 17 L12 22 L8 30"/>
      <path d="M24 16 L32 24 L40 24"/>
    </g>
  </svg>

  <p class="visit-note">Come in<br>person to<br>submit your<br>ballot to<br>Pinecrest Road,<br>conveniently<br>located on the<br>3rd floor of the<br>Marden Family<br>Health Centre.</p>

  <div class="ballot">
    <div class="ballot-row">Name <span class="ballot-line"></span></div>
    <div class="ballot-row">Phone <span class="ballot-line"></span></div>
  </div>

  <div class="prize">$1000</div>
  <div class="prize-note">TRAVEL GIFT CARD</div>

  <p class="contest-details">Competition closes<br>July 15, 2019<br><span class="call-to-action">Stop, meet the team,<br>sign in to win!</span></p>

  <div class="contact">
    <svg class="contact-icon" style="left:35px;top:12px" width="30" height="46" viewBox="0 0 30 46" aria-hidden="true">
      <path d="M10 2 L18 2 L16 12 L11 14 Q9 23 11 32 L16 34 L18 44 L10 44 Q2 40 2 23 Q2 6 10 2 Z" fill="#1e1c1d"/>
    </svg>
    <svg class="contact-icon" style="left:38px;top:66px" width="28" height="20" viewBox="0 0 28 20" aria-hidden="true">
      <rect x="1.5" y="1.5" width="25" height="17" fill="none" stroke="#1e1c1d" stroke-width="2"/>
      <path d="M1.5 1.5 L14 11 L26.5 1.5 M1.5 18.5 L11 9 M26.5 18.5 L17 9" fill="none" stroke="#1e1c1d" stroke-width="2"/>
    </svg>
    <div class="phone">905-418-2735</div>
    <div class="web">www.brightwaydental.ca</div>
    <div class="address">1846 Pinecrest Road, Burlington,<br>Ontario, L7N 2R8</div>
  </div>

</div>
</body>
</html>
```